Brackenridge Strength Studio Chronic Pain Flyer

Double sided DL flyer required to promote a strength training studio to sufferers of chronic pain. Flyer will be displayed in osteopathy, chiropractic and massage clinics. Flyer should be clean, professional and appeal to an older (40+) demographic.

Target Market(s)

Chronic pain sufferers. Age 40+

Industry/Entity Type

Health And Wellness

Colors

Designer to choose colors to be used in the design.

Requirements
Must have
• See attached files for text copy and logo. Image(s) of people strength training with a coach or personal trainer, as well as images depicting pain in common parts of the body (such as those pictured in the supplied mock up)
• website address: brackenridgestrengthstudio.example.com.au
• phone number : 0452 918 304
• Street address: 4/63 Juniper Hollow Rd, Brackenridge
Nice to have
• Images such as in the attached files.

```html
<!DOCTYPE html>
<html lang="en">
<head>
<meta charset="utf-8">
<title>Brackenridge Strength Studio – Chronic Pain Flyer</title>
<link href="https://fonts.googleapis.com/css2?family=Lato:wght@400;700;900&display=swap" rel="stylesheet">
<style>
  :root{
    --stage:#3a3a3a;
    --red:#d42027;
    --white:#ffffff;
    --paper:#fbfbfb;
    --ink:#111111;
    --grey:#9a9a9a;
    --grey-light:#c9c9c9;
    --label:#f2f2f2;
  }
  *{box-sizing:border-box;margin:0;padding:0}
  html,body{width:1200px;height:1200px;overflow:hidden;background:var(--stage);font-family:"Lato",sans-serif}
  .flyer{position:absolute;top:127px;width:443px;height:911px;background:var(--white);overflow:hidden;box-shadow:0 4px 14px rgba(0,0,0,.35)}
  .flyer--front{left:124px}
  .flyer--back{left:637px;background:var(--paper)}
  .side-label{position:absolute;top:1075px;width:443px;text-align:center;color:var(--label);font-size:38px;font-weight:400}
  .side-label--front{left:105px}
  .side-label--back{left:622px}

  .brand{position:absolute;left:0;width:100%;text-align:center;color:#555;font-weight:900;line-height:1.05;text-transform:uppercase;letter-spacing:1px}
  .brand span{display:block}
  .flyer--front .brand{top:72px;font-size:27px}
  .flyer--back .brand{top:652px;font-size:21px;z-index:2}

  .photo{position:absolute;left:0;top:160px;width:100%;height:440px;background:linear-gradient(120deg,#d6d9dc 0%,#c4c8cc 45%,#7d8fb8 75%,#2d5fb8 100%)}
  .shape{position:absolute;left:0;width:100%}

  .headline{position:absolute;left:0;width:100%;text-align:center;text-transform:uppercase;line-height:1}
  .headline .lead{display:block;font-weight:700;letter-spacing:-.5px}
  .headline .main{display:block;font-weight:900;letter-spacing:-1px}
  .flyer--front .headline{top:631px;color:var(--white)}
  .flyer--front .lead{font-size:46px}
  .flyer--front .main{font-size:78px;margin-top:2px}
  .flyer--back .headline{top:32px;color:var(--ink)}
  .flyer--back .lead{font-size:44px}
  .flyer--back .main{font-size:74px;margin-top:0}

  .red-block{position:absolute;left:0;width:100%;background:var(--red)}
  .tagline{position:absolute;left:0;top:167px;width:100%;height:47px;background:var(--red);color:var(--white);font-size:29px;font-weight:700;text-align:center;line-height:47px}

  .copy{position:absolute;left:26px;width:393px;font-size:20px;line-height:25px;text-align:justify;color:var(--ink)}
  .copy--intro{top:225px}
  .copy--offer{top:485px}

  .pain-spots{position:absolute;top:342px;left:14px;width:415px;display:flex;justify-content:space-between}
  .pain-spot{width:126px;height:126px;border-radius:50%;border:3px solid var(--red);background:radial-gradient(circle at 50% 62%,#f08a8e 0%,#d8d8d8 30%,#a9a9a9 70%,#efefef 100%)}

  .contact{position:absolute;left:0;width:100%;text-align:center}
  .contact-phone{display:flex;align-items:center;justify-content:center;gap:8px;font-size:38px;font-weight:900;letter-spacing:-.5px}
  .contact-line{display:flex;align-items:center;justify-content:center;gap:10px;font-size:16px;margin-top:10px}
  .contact svg{flex:none}
  .flyer--front .contact{top:768px;color:#222}
  .flyer--front .contact-phone{color:var(--red)}
  .flyer--back .contact{top:770px;color:var(--white);z-index:2}
</style>
</head>
<body>

<section class="flyer flyer--front">
  <div class="brand"><span>Brackenridge</span><span>Strength Studio</span></div>
  <div class="photo" role="img" aria-label="Coach guiding an older client lifting a dumbbell"></div>
  <svg class="shape" style="top:150px" width="443" height="40" viewBox="0 0 443 40" aria-hidden="true">
    <path d="M0 0 H443 V12 Q221 40 0 22 Z" fill="#ffffff"/>
    <path d="M0 22 Q221 40 443 12" fill="none" stroke="#a9a9a9" stroke-width="3"/>
  </svg>
  <svg class="shape" style="top:520px" width="443" height="90" viewBox="0 0 443 90" aria-hidden="true">
    <path d="M0 10 Q221 70 443 0 V90 H0 Z" fill="#a9a9a9"/>
    <path d="M0 30 Q221 80 443 30 V90 H0 Z" fill="#d42027"/>
  </svg>
  <div class="red-block" style="top:605px;height:156px"></div>
  <h1 class="headline"><span class="lead">Health Through</span><span class="main">Strength</span></h1>
  <div class="red-block" style="top:887px;height:24px"></div>
  <div class="contact">
    <div class="contact-phone">
      <svg width="34" height="34" viewBox="0 0 34 34" aria-hidden="true"><circle cx="17" cy="17" r="15.5" fill="none" stroke="#888" stroke-width="2"/><path d="M11 9 l4 0 1 5-2.5 1.5c1 2.5 3 4.5 5.5 5.5L20.5 18l5 1v4c0 1-1 2-2 2C15 24 10 19 9 11c0-1 1-2 2-2z" fill="none" stroke="#888" stroke-width="1.8"/></svg>
      <span>0452 918 304</span>
    </div>
    <div class="contact-line">
      <svg width="20" height="20" viewBox="0 0 20 20" aria-hidden="true"><g fill="none" stroke="#888" stroke-width="1.4"><circle cx="10" cy="10" r="8.5"/><ellipse cx="10" cy="10" rx="3.8" ry="8.5"/><path d="M1.5 10h17M3 5.5h14M3 14.5h14"/></g></svg>
      <span>brackenridgestrengthstudio.example.com.au</span>
    </div>
    <div class="contact-line">
      <svg width="16" height="20" viewBox="0 0 16 20" aria-hidden="true"><path d="M8 1a6 6 0 0 0-6 6c0 4.5 6 12 6 12s6-7.5 6-12a6 6 0 0 0-6-6zm0 8.2a2.2 2.2 0 1 1 0-4.4 2.2 2.2 0 0 1 0 4.4z" fill="#888"/></svg>
      <span>4/63 Juniper Hollow Rd, Brackenridge</span>
    </div>
  </div>
</section>

<section class="flyer flyer--back">
  <h2 class="headline"><span class="lead">Health Through</span><span class="main">Strength</span></h2>
  <p class="tagline">You Don’t have to live in pain.</p>
  <p class="copy copy--intro">Strength taining has been shown to improve many chronic pain conditions and is now being routinely recommended by medical and health professionals.</p>
  <div class="pain-spots">
    <div class="pain-spot" role="img" aria-label="Lower back pain highlighted in red"></div>
    <div class="pain-spot" role="img" aria-label="Shoulder pain highlighted in red"></div>
    <div class="pain-spot" role="img" aria-label="Knee pain highlighted in red"></div>
  </div>
  <p class="copy copy--offer">Our private studio provides high quality strength training by expert strength coaches. We’ve helped countless people improve or eliminate chronic pain, contact us today and find out how we can help you.</p>
  <svg class="shape" style="top:675px" width="443" height="236" viewBox="0 0 443 236" aria-hidden="true">
    <path d="M0 0 Q221 110 443 0 V236 H0 Z" fill="#a9a9a9"/>
    <path d="M0 28 Q221 120 443 28 V236 H0 Z" fill="#d42027"/>
  </svg>
  <div class="brand"><span>Brackenridge</span><span>Strength Studio</span></div>
  <div class="contact">
    <div class="contact-phone">
      <svg width="34" height="34" viewBox="0 0 34 34" aria-hidden="true"><circle cx="17" cy="17" r="15.5" fill="none" stroke="#fff" stroke-width="2"/><path d="M11 9 l4 0 1 5-2.5 1.5c1 2.5 3 4.5 5.5 5.5L20.5 18l5 1v4c0 1-1 2-2 2C15 24 10 19 9 11c0-1 1-2 2-2z" fill="none" stroke="#fff" stroke-width="1.8"/></svg>
      <span>0452 918 304</span>
    </div>
    <div class="contact-line">
      <svg width="20" height="20" viewBox="0 0 20 20" aria-hidden="true"><g fill="none" stroke="#fff" stroke-width="1.4"><circle cx="10" cy="10" r="8.5"/><ellipse cx="10" cy="10" rx="3.8" ry="8.5"/><path d="M1.5 10h17M3 5.5h14M3 14.5h14"/></g></svg>
      <span>brackenridgestrengthstudio.example.com.au</span>
    </div>
    <div class="contact-line" style="margin-top:6px">
      <svg width="16" height="20" viewBox="0 0 16 20" aria-hidden="true"><path d="M8 1a6 6 0 0 0-6 6c0 4.5 6 12 6 12s6-7.5 6-12a6 6 0 0 0-6-6zm0 8.2a2.2 2.2 0 1 1 0-4.4 2.2 2.2 0 0 1 0 4.4z" fill="#fff"/></svg>
      <span>4/63 Juniper Hollow Rd, Brackenridge</span>
    </div>
  </div>
</section>

<p class="side-label side-label--front">Front</p>
<p class="side-label side-label--back">Back</p>

</body>
</html>
```